PowerPoint Template Needed for Investment Firm

Norvelle Capital Management is an emerging wealth management firm based in New Jersey. It offers superior investment returns to high net worth individuals and institutions by finding undervalued assets.

We recently selected a company logo which was inspired by the Tucana constellation. Beta Tucanae is a group of six stars, containing star cluster 47 Tucanae, rated the second brightest object in the sky.

Now we need a PowerPoint template with the designs for the following:

1. Title/cover page slide
2. Content slide with title
3. Section slide - to introduce a new section
4. Final slide - with contact information

The slides will be used at investor presentations, that is, to provide information about the company to potential investors. Since we are an investment firm, the design should project a sense of stability, growth and professionalism. The owner is interested in something simple yet striking, which of course is consistent with the logo. I'm thinking more conservative colors and Sans Serif fonts.

I plan on changing the status to non-refundable once I see some designs that I really like.

Target Market(s)

Wealthy individuals, probably middle aged or older, in the US

Industry/Entity Type

Conservative

Requirements
Must have
• Sans serif fonts
Clean, very professional look
Conservative colors that complement existing logo
Should not have
• Anything too busy or complicated

```html
<!DOCTYPE html>
<html lang="en">
<head>
<meta charset="utf-8">
<title>Norvelle Capital Management – Title Slide</title>
<link href="https://fonts.googleapis.com/css2?family=Arimo:wght@400&display=swap" rel="stylesheet">
<style>
  :root {
    --band-top: #1a46b0;
    --band-bottom: #061a7a;
    --band-edge: #3f6fd6;
    --navy: #0a1a6e;
    --ink: #111111;
    --white: #ffffff;
    --frame: #2a52b8;
    --placeholder: #7a7a7a;
    --map-light: #3a64c8;
  }
  * { margin: 0; padding: 0; box-sizing: border-box; }
  html, body {
    width: 1200px; height: 900px; overflow: hidden;
    background: var(--white);
    font-family: "Arimo", Arial, sans-serif;
  }
  .slide {
    position: relative; width: 1200px; height: 900px;
    background: var(--white);
    border-left: 3px solid var(--frame);
    border-right: 3px solid var(--frame);
  }
  .header-band {
    position: absolute; left: 0; top: 0; width: 100%; height: 402px;
    background: linear-gradient(to bottom, var(--band-top) 0%, var(--band-bottom) 100%);
    border-bottom: 4px solid var(--band-edge);
  }
  .brand-card {
    position: absolute; left: 28px; top: 174px; width: 304px; height: 228px;
    background: var(--white);
    border-radius: 16px 16px 0 0;
    display: flex; flex-direction: column; align-items: center; justify-content: center;
    gap: 18px;
  }
  .brand-mark {
    width: 96px; height: 96px; border-radius: 14px;
    background: var(--band-bottom);
  }
  .brand-name {
    color: var(--navy); font-size: 25px; font-weight: 400;
    text-align: center; line-height: 1.2;
  }
  .state-map {
    position: absolute; left: 957px; top: 38px; width: 209px; height: 326px;
    background: radial-gradient(ellipse at 50% 50%, var(--map-light) 0%, rgba(58,100,200,0) 70%);
    opacity: 0.55;
  }
  .field {
    position: absolute; left: 32px;
    border: 1.5px dotted var(--placeholder);
    display: flex; align-items: center; padding-left: 2px;
    white-space: nowrap;
  }
  .title {
    top: 470px; width: 1134px; height: 65px;
    color: var(--navy); font-size: 49px;
  }
  .subtitle {
    top: 567px; width: 1134px; height: 42px;
    color: var(--ink); font-size: 28px;
  }
  .doc-type {
    top: 722px; width: 368px; height: 33px;
    color: var(--ink); font-size: 24px;
  }
  .doc-date {
    top: 772px; width: 368px; height: 34px;
    color: var(--ink); font-size: 24px;
  }
  .page-number {
    position: absolute; right: 6px; top: 846px;
    font-size: 21px; color: var(--ink);
  }
  .footer-band {
    position: absolute; left: -3px; bottom: 0; width: 1200px; height: 32px;
    background: var(--band-bottom);
  }
</style>
</head>
<body>
  <main class="slide">
    <header class="header-band">
      <div class="brand-card">
        <div class="brand-mark"></div>
        <div class="brand-name">Norvelle<br>Capital Management</div>
      </div>
      <div class="state-map" role="img" aria-label="Outline map of New Jersey"></div>
    </header>

    <h1 class="field title" style="font-weight:400;">Presentation title</h1>
    <p class="field subtitle">Subtitle</p>
    <p class="field doc-type">Document type</p>
    <p class="field doc-date">Date</p>

    <span class="page-number">1</span>
    <footer class="footer-band"></footer>
  </main>
</body>
</html>
```